Kelvora trustee touch - styling

We have a prototyped single page application. The content is in place what we need is restyling to

- make it more user friendly
- modern look and feel
- improve accessibility features
- use our brand guidelines (screen shots attached of the full website)

Prototype is available at http://plinthdesk.examplehost.net/

Target form factor:
Primary - tablet
Secondary - desktop

Target Market(s)

Business users - not financial professionals but people working for big companies who have some limited training in the concepts

Number of Pages Required

1 page

Requirements
Must have
• Touch user interface

```html
<!DOCTYPE html>
<html lang="en">
<head>
<meta charset="utf-8">
<title>Kelvora Dashboard</title>
<link rel="stylesheet" href="https://fonts.googleapis.com/css2?family=Arimo:wght@400;700&display=swap">
<style>
:root{
  --brand:#1466c2;
  --brand-dark:#0e56a8;
  --brand-deep:#0b4c96;
  --brand-line:#2a78cf;
  --accent-blue:#2d6db5;
  --green:#3fa52f;
  --green-dark:#2f8f21;
  --purple:#7b56c9;
  --purple-dark:#6a45b7;
  --orange:#e8693a;
  --orange-dark:#d6542a;
  --ink:#222;
  --muted:#9aa3ad;
  --rule:#e3e6ea;
  --row:#f6f7f9;
  --row-hi:#edf1f6;
  --chart-blue:#3b86d6;
  --chart-orange:#ea6a3c;
  --fill-blue:#eef5fb;
  --fill-orange:#f9e7e1;
  --tooltip:#222;
  --white:#fff;
}
*{box-sizing:border-box;margin:0;padding:0}
html,body{width:1200px;height:729px;overflow:hidden}
body{font-family:"Arimo",Arial,sans-serif;color:var(--ink);background:var(--white);position:relative}
.topbar{position:absolute;left:0;top:0;width:1200px;height:37px;background:var(--brand)}
.brand{position:absolute;left:0;top:0;width:144px;height:37px;background:var(--brand-dark);color:var(--white);font-weight:700;font-size:24px;line-height:37px;padding-left:22px;letter-spacing:-.5px}
.menu-toggle{position:absolute;left:152px;top:11px}
.user{position:absolute;left:1030px;top:0;height:37px;width:100px;border-left:1px solid var(--brand-line);border-right:1px solid var(--brand-line);color:var(--white);font-size:8px;line-height:37px}
.avatar{position:absolute;left:14px;top:12px;width:14px;height:13px;background:linear-gradient(#9a7b6a,#5a4a44);border-radius:1px}
.user span{position:absolute;left:35px}
.user svg{position:absolute;left:80px;top:16px}
.top-icon{position:absolute;top:13px}
.top-divider{position:absolute;left:1165px;top:0;width:1px;height:37px;background:var(--brand-line)}
.sidebar{position:absolute;left:0;top:37px;width:144px;height:661px;background:var(--brand)}
.nav a{display:block;height:40px;line-height:40px;padding-left:17px;color:var(--white);font-size:7.5px;font-weight:700;text-decoration:none;border-bottom:1px solid var(--brand-line);letter-spacing:.2px}
.nav a.active{background:var(--brand-dark);border-left:3px solid #4b95e0;padding-left:14px}
.settings{position:absolute;top:450px;left:0;width:144px;height:106px;border-bottom:1px solid var(--brand-line)}
.settings h4{font-size:7.5px;color:var(--white);padding:3px 0 0 17px;font-weight:700}
.settings a{display:flex;align-items:center;gap:6px;color:var(--white);font-size:7.5px;text-decoration:none;padding-left:20px;height:25px}
.footer{position:absolute;left:0;top:698px;width:1200px;height:31px;background:var(--brand-deep);display:flex;align-items:center;padding-left:16px;gap:22px}
.footer a{color:#cfe0f5;font-size:11px;text-decoration:none;letter-spacing:.3px}
.stat{position:absolute;top:63px;width:320px;height:120px;color:var(--white)}
.stat .label{position:absolute;left:22px;top:21px;font-size:12px;letter-spacing:.2px}
.stat .value{position:absolute;left:21px;top:41px;font-size:32px;font-weight:700}
.stat .note{position:absolute;left:0;bottom:0;width:100%;height:30px;line-height:31px;padding-left:22px;font-size:12px}
.stat .bars{position:absolute;right:18px;top:21px}
.sales{left:174px;background:var(--green)}.sales .note{background:var(--green-dark)}
.orders{left:514px;background:var(--purple)}.orders .note{background:var(--purple-dark)}
.visits{left:855px;width:319px;background:var(--orange)}.visits .note{background:var(--orange-dark)}
.panel-title{position:absolute;font-size:15px;font-weight:700;color:var(--ink)}
.rule{position:absolute;height:1px;background:var(--rule)}
.tabs{position:absolute;left:570px;top:223px;display:flex;gap:8px;font-size:12px}
.tabs span{height:23px;line-height:23px;padding:0 8px;color:var(--accent-blue)}
.tabs .on{background:var(--accent-blue);color:var(--white);border-radius:12px;padding:0 15px}
.vline{position:absolute;width:1px;background:var(--rule)}
.chart{position:absolute;left:175px;top:285px}
.chart text{font-family:"Arimo",Arial,sans-serif;font-size:10px;fill:#c9ced4}
.tooltip{position:absolute;left:358px;top:366px;width:120px;height:45px;background:var(--tooltip);color:var(--white);padding:9px 0 0 12px}
.tooltip small{display:block;font-size:11px;color:#bbb}
.tooltip strong{display:block;font-size:15px;margin-top:2px}
.tooltip::after{content:"";position:absolute;left:55px;bottom:-6px;border:6px solid transparent;border-bottom:0;border-top-color:var(--tooltip)}
.pill-cut{position:absolute;left:807px;top:559px;width:60px;height:23px;border-radius:12px;background:var(--accent-blue);color:var(--white);font-size:12px;line-height:23px;padding-left:15px}
.todos{position:absolute;left:848px;top:265px;width:328px;height:330px;background:var(--white)}
.todos h3{position:absolute;left:21px;top:20px;font-size:15px}
.badge{position:absolute;left:70px;top:17px;width:28px;height:24px;border-radius:12px;background:var(--green);color:var(--white);font-size:11px;text-align:center;line-height:24px}
.todo{position:absolute;left:0;width:328px;height:33px;background:var(--row);border-bottom:1px solid #eceef1;font-size:12px;line-height:33px;padding-left:45px;color:#333}
.todo.hi{background:var(--row-hi)}
.todo .grip{position:absolute;left:0;top:12px;width:8px;height:9px;background:repeating-linear-gradient(#c8ccd1 0 1.5px,transparent 1.5px 3.5px)}
.todo .box{position:absolute;left:20px;top:7px;width:18px;height:18px;border:1.5px solid #bfc4ca;border-radius:3px;background:var(--white)}
.todo .box.focus{border-color:var(--accent-blue)}
.todo .box.done{border-color:var(--green)}
.todo .close{position:absolute;right:10px;top:0;color:#c5c9ce;font-size:14px}
.todo.done-row{color:var(--green);text-decoration:line-through}
.add{position:absolute;left:21px;top:198px;font-size:11px;color:#bfc4ca}
.report{position:absolute;top:628px;width:230px;height:48px}
.report svg{position:absolute;left:0;top:0}
.report .k{position:absolute;left:114px;top:1px;font-size:10px;color:var(--muted);letter-spacing:.3px}
.report .v{position:absolute;left:114px;top:14px;font-size:27px;font-weight:700}
</style>
</head>
<body>
<header class="topbar">
  <div class="brand">Kelvora</div>
  <svg class="menu-toggle" width="26" height="14" viewBox="0 0 26 14" aria-label="Toggle menu"><path d="M5 2 1 7l4 5" stroke="#fff" stroke-width="2" fill="none"/><rect x="11" y="1" width="13" height="2.4" fill="#fff"/><rect x="11" y="6" width="13" height="2.4" fill="#fff"/><rect x="11" y="11" width="13" height="2.4" fill="#fff"/></svg>
  <div class="user"><div class="avatar" role="img" aria-label="User avatar"></div><span>Hi, Doran</span><svg width="8" height="6" viewBox="0 0 8 6"><path d="M1 1l3 3 3-3" stroke="#fff" stroke-width="1.6" fill="none"/></svg></div>
  <svg class="top-icon" style="left:1143px" width="9" height="10" viewBox="0 0 9 10" aria-label="Profile"><circle cx="4.5" cy="3" r="2.5" fill="#cfe0f5"/><path d="M0 10c0-3 2-4.5 4.5-4.5S9 7 9 10z" fill="#cfe0f5"/></svg>
  <div class="top-divider"></div>
  <svg class="top-icon" style="left:1179px" width="9" height="10" viewBox="0 0 9 10" aria-label="Lock"><path d="M2 4V3a2.5 2.5 0 0 1 5 0v1" stroke="#cfe0f5" stroke-width="1.3" fill="none"/><rect x="0.5" y="4" width="8" height="6" rx="1" fill="#cfe0f5"/></svg>
</header>

<aside class="sidebar">
  <nav class="nav">
    <a class="active" href="#">DASHBOARD</a>
    <a href="#">ANALYTICS</a>
    <a href="#">RISK</a>
    <a href="#">ALM</a>
    <a href="#">OPTIMIZER</a>
    <a href="#">CURVES</a>
    <a href="#">ADMIN</a>
  </nav>
  <div class="settings">
    <h4>SETTINGS</h4>
    <a href="#"><svg width="10" height="11" viewBox="0 0 10 11"><path d="M1 1h8M1 10h8M2 1c0 3 6 3 6 9M8 1c0 3-6 3-6 9" stroke="#9cc4ee" stroke-width="1.2" fill="none"/></svg>Tools</a>
    <a href="#"><svg width="13" height="11" viewBox="0 0 13 11"><path d="M2 0v11M6.5 0v11M11 0v11" stroke="#9cc4ee"/><rect x="0.5" y="6" width="3" height="2" fill="#9cc4ee"/><rect x="5" y="2" width="3" height="2" fill="#9cc4ee"/><rect x="9.5" y="5" width="3" height="2" fill="#9cc4ee"/></svg>Configurations</a>
    <a href="#"><svg width="15" height="10" viewBox="0 0 15 10"><circle cx="4" cy="3" r="2" fill="#9cc4ee"/><circle cx="11" cy="3" r="2" fill="#9cc4ee"/><circle cx="7.5" cy="2.5" r="2.3" fill="#9cc4ee"/><path d="M0 10c0-3 2-4 4-4s4 1 4 4zM7 10c0-3 2-4 4-4s4 1 4 4zM3 10c0-3.5 2-4.5 4.5-4.5S12 6.5 12 10z" fill="#9cc4ee"/></svg>User Access</a>
  </div>
</aside>

<section class="stat sales">
  <div class="label">TODAY'S SALES</div>
  <div class="value">$21,561.01</div>
  <svg class="bars" width="96" height="48" viewBox="0 0 96 48" aria-hidden="true" fill="rgba(255,255,255,.5)"><rect x="0" y="8" width="4" height="40"/><rect x="8" y="18" width="4" height="30"/><rect x="16" y="28" width="4" height="20"/><rect x="24" y="14" width="4" height="34"/><rect x="32" y="22" width="4" height="26"/><rect x="40" y="12" width="4" height="36"/><rect x="48" y="18" width="4" height="30"/><rect x="56" y="24" width="4" height="24"/><rect x="64" y="14" width="4" height="34"/><rect x="72" y="6" width="4" height="42"/><rect x="80" y="16" width="4" height="32"/><rect x="88" y="20" width="4" height="28"/></svg>
  <div class="note">44% Higher Than Yesterday</div>
</section>
<section class="stat orders">
  <div class="label">TODAY'S ORDERS</div>
  <div class="value">17,561</div>
  <svg class="bars" width="96" height="48" viewBox="0 0 96 48" aria-hidden="true" fill="#fff"><rect x="0" y="34" width="4" height="14"/><rect x="8" y="38" width="4" height="10"/><rect x="16" y="26" width="4" height="22"/><rect x="24" y="36" width="4" height="12"/><rect x="32" y="22" width="4" height="26"/><rect x="40" y="14" width="4" height="34"/><rect x="48" y="24" width="4" height="24"/><rect x="56" y="6" width="4" height="42"/><rect x="64" y="18" width="4" height="30"/><rect x="72" y="4" width="4" height="44"/><rect x="80" y="20" width="4" height="28"/><rect x="88" y="14" width="4" height="34"/></svg>
  <div class="note">20% Higher Than Yesterday</div>
</section>
<section class="stat visits">
  <div class="label">TODAY'S VISITS</div>
  <div class="value">2,545,665</div>
  <svg class="bars" width="96" height="48" viewBox="0 0 96 48" aria-hidden="true" fill="#fff"><rect x="0" y="34" width="4" height="14"/><rect x="8" y="38" width="4" height="10"/><rect x="16" y="26" width="4" height="22"/><rect x="24" y="36" width="4" height="12"/><rect x="32" y="22" width="4" height="26"/><rect x="40" y="14" width="4" height="34"/><rect x="48" y="24" width="4" height="24"/><rect x="56" y="6" width="4" height="42"/><rect x="64" y="18" width="4" height="30"/><rect x="72" y="4" width="4" height="44"/><rect x="80" y="20" width="4" height="28"/><rect x="88" y="14" width="4" height="34"/></svg>
  <div class="note">12% Higher Than Yesterday</div>
</section>

<h2 class="panel-title" style="left:176px;top:225px">Visitors</h2>
<div class="tabs"><span class="on">Today</span><span>Yesterday</span><span>Month</span></div>
<div class="vline" style="left:770px;top:207px;height:52px"></div>
<svg style="position:absolute;left:789px;top:225px" width="18" height="18" viewBox="0 0 18 18" aria-label="Calendar"><rect x="1" y="3" width="16" height="14" rx="1.5" fill="none" stroke="var(--accent-blue)" stroke-width="2"/><rect x="1" y="3" width="16" height="4" fill="var(--accent-blue)"/><rect x="4" y="0" width="2" height="4" fill="var(--accent-blue)"/><rect x="12" y="0" width="2" height="4" fill="var(--accent-blue)"/></svg>
<div class="rule" style="left:152px;top:259px;width:674px"></div>

<svg class="chart" width="630" height="250" viewBox="175 285 630 250" aria-label="Visitors chart">
  <path fill="var(--fill-blue)" d="M175,462 C195,462 195,457 215,457 C241,457 241,392 268,392 C293,392 293,389 319,389 C343,389 343,400 367,400 C393,400 393,362 419,362 C447,362 447,298 476,298 C503,298 503,350 531,350 C557,350 557,367 584,367 C609,367 609,332 635,332 C660,332 660,345 685,345 C710,345 710,388 736,388 C757,388 757,383 778,383 C790,383 790,368 803,368 L803,530 L175,530 Z"/>
  <path fill="var(--fill-orange)" d="M175,466 C195,466 195,486 215,486 C241,486 241,506 268,506 C293,506 293,510 319,510 C344,510 344,473 370,473 C394,473 394,430 419,430 C447,430 447,411 476,411 C503,411 503,421 531,421 C557,421 557,446 584,446 C609,446 609,463 635,463 C660,463 660,459 685,459 C710,459 710,427 736,427 C757,427 757,391 778,391 C790,391 790,376 803,376 L803,530 L175,530 Z"/>
  <g>
    <text x="177" y="303">10</text><text x="177" y="328">20</text><text x="177" y="353">30</text><text x="177" y="378">40</text><text x="177" y="402">50</text><text x="177" y="427">60</text><text x="177" y="452">70</text><text x="177" y="477">80</text><text x="177" y="502">90</text><text x="177" y="527">100</text>
    <text x="210" y="527">10</text><text x="249" y="527">20</text><text x="288" y="527">30</text><text x="327" y="527">40</text><text x="365" y="527">50</text><text x="404" y="527">60</text><text x="443" y="527">70</text><text x="482" y="527">80</text><text x="520" y="527">90</text><text x="556" y="527">100</text><text x="600" y="527">110</text><text x="643" y="527">120</text><text x="688" y="527">130</text><text x="733" y="527">140</text><text x="777" y="527">150</text>
  </g>
  <path fill="none" stroke="var(--chart-blue)" stroke-width="1.5" d="M175,462 C195,462 195,457 215,457 C241,457 241,392 268,392 C293,392 293,389 319,389 C343,389 343,400 367,400 C393,400 393,362 419,362 C447,362 447,298 476,298 C503,298 503,350 531,350 C557,350 557,367 584,367 C609,367 609,332 635,332 C660,332 660,345 685,345 C710,345 710,388 736,388 C757,388 757,383 778,383 C790,383 790,368 803,368"/>
  <path fill="none" stroke="var(--chart-orange)" stroke-width="1.5" d="M175,466 C195,466 195,486 215,486 C241,486 241,506 268,506 C293,506 293,510 319,510 C344,510 344,473 370,473 C394,473 394,430 419,430 C447,430 447,411 476,411 C503,411 503,421 531,421 C557,421 557,446 584,446 C609,446 609,463 635,463 C660,463 660,459 685,459 C710,459 710,427 736,427 C757,427 757,391 778,391 C790,391 790,376 803,376"/>
  <g fill="#fff" stroke="var(--chart-blue)" stroke-width="1.6">
    <circle cx="215" cy="457" r="3.3"/><circle cx="268" cy="392" r="3.3"/><circle cx="319" cy="389" r="3.3"/><circle cx="419" cy="362" r="3.3"/><circle cx="476" cy="298" r="3.3"/><circle cx="531" cy="350" r="3.3"/><circle cx="584" cy="367" r="3.3"/><circle cx="635" cy="332" r="3.3"/><circle cx="685" cy="345" r="3.3"/><circle cx="736" cy="388" r="3.3"/><circle cx="778" cy="383" r="3.3"/>
  </g>
  <g fill="#fff" stroke="var(--chart-orange)" stroke-width="1.6">
    <circle cx="215" cy="486" r="3.3"/><circle cx="268" cy="506" r="3.3"/><circle cx="319" cy="510" r="3.3"/><circle cx="370" cy="473" r="3.3"/><circle cx="419" cy="430" r="4.5" stroke-width="2.5"/><circle cx="476" cy="411" r="3.3"/><circle cx="531" cy="421" r="3.3"/><circle cx="584" cy="446" r="3.3"/><circle cx="635" cy="463" r="3.3"/><circle cx="685" cy="459" r="3.3"/><circle cx="736" cy="427" r="3.3"/><circle cx="778" cy="391" r="3.3"/>
  </g>
</svg>
<div class="tooltip"><small>12 Oct 2013</small><strong>2384 Visitors</strong></div>

<h2 class="panel-title" style="left:175px;top:561px">Site Reports</h2>
<div class="pill-cut">Today</div>
<div class="rule" style="left:152px;top:594px;width:696px"></div>

<section class="todos">
  <h3>Todos</h3><span class="badge">34</span>
  <div class="vline" style="left:270px;top:2px;height:52px"></div>
  <svg style="position:absolute;left:290px;top:19px" width="20" height="20" viewBox="0 0 20 20" aria-label="Refresh"><path d="M16 10a6 6 0 1 1-2-4.5" fill="none" stroke="var(--accent-blue)" stroke-width="2.2"/><path d="M11 3h6v6z" fill="var(--accent-blue)"/></svg>
  <div class="rule" style="left:0;top:54px;width:328px"></div>
  <div class="todo" style="top:55px"><i class="grip"></i><i class="box"></i>Quae vero auctorem tractata ab fiducia...<span class="close">×</span></div>
  <div class="todo" style="top:88px"><i class="grip"></i><i class="box"></i>Cum ceteris in, nascetur mus.<span class="close">×</span></div>
  <div class="todo hi" style="top:121px"><i class="grip"></i><i class="box focus"></i>Ut enim ad minim veniam exercitation.<span class="close">×</span></div>
  <div class="todo done-row" style="top:155px"><i class="grip"></i><svg class="box done" style="position:absolute;left:20px;top:7px;width:18px;height:18px;border:1.5px solid var(--green);border-radius:3px;background:#fff" viewBox="0 0 18 18"><path d="M3 9l4 4 8-9" fill="none" stroke="var(--green)" stroke-width="2.2"/></svg>Hi omnes lingua, institutis inter se differunt.<span class="close" style="text-decoration:none">×</span></div>
  <div class="add">Add to do...</div>
</section>

<div class="report" style="left:177px">
  <svg width="100" height="46" viewBox="0 0 100 46"><path d="M0,10 C30,12 35,30 50,30 C65,30 70,2 100,0 L100,46 L0,46Z" fill="#e0f5dc"/><path d="M0,10 C30,12 35,30 50,30 C65,30 70,2 100,0" fill="none" stroke="var(--green)"/></svg>
  <span class="k">VISITS</span><span class="v" style="color:var(--green)">7,451</span>
</div>
<div class="report" style="left:406px">
  <svg width="100" height="46" viewBox="0 0 100 46"><path d="M0,10 C30,12 35,30 50,30 C65,30 70,2 100,0 L100,46 L0,46Z" fill="#eef4fb"/><path d="M0,10 C30,12 35,30 50,30 C65,30 70,2 100,0" fill="none" stroke="var(--chart-blue)"/></svg>
  <span class="k">PAGE VIEWS</span><span class="v" style="color:var(--accent-blue)">35,711</span>
</div>
<div class="report" style="left:651px">
  <svg width="100" height="46" viewBox="0 0 100 46"><path d="M0,10 C30,12 35,30 50,30 C65,30 70,2 100,0 L100,46 L0,46Z" fill="#f9e6e0"/><path d="M0,10 C30,12 35,30 50,30 C65,30 70,2 100,0" fill="none" stroke="var(--chart-orange)"/></svg>
  <span class="k">AVERAGE TIME</span><span class="v" style="color:var(--orange)">00:04:17</span>
</div>
<div class="report" style="left:930px">
  <svg width="100" height="46" viewBox="0 0 100 46"><path d="M0,10 C30,12 35,30 50,30 C65,30 70,2 100,0 L100,46 L0,46Z" fill="#ede8f8"/><path d="M0,10 C30,12 35,30 50,30 C65,30 70,2 100,0" fill="none" stroke="var(--purple)"/></svg>
  <span class="k">BOUNCE RATE</span><span class="v" style="color:var(--purple-dark)">31.08%</span>
</div>

<footer class="footer">
  <a href="#">HELP</a><a href="#">ABOUT US</a><a href="#">TERM AND CONDITIONS</a><a href="#">CONTACT US</a>
</footer>
</body>
</html>
```